Amber Ridge Publishing Web Page Design

Design a website for my new start up publishing company - Amber Ridge Publishing, the first work published by ARP with be a new book by M.R. Theodor called Silent Ledger. The prototype for the book cover is attached.

Target Market(s)

Worldwide, all readers of mystery, fiction, etc.

Industry/Entity Type

Book Publisher

Coding

Coded - Design and coding required

Number of Pages Required

1 page

```html
<!DOCTYPE html>
<html lang="en">
<head>
<meta charset="UTF-8">
<title>Amber Ridge Publishing</title>
<link href="https://fonts.googleapis.com/css2?family=Roboto:wght@300;400;500;700&family=Open+Sans:wght@400;600;700&display=swap" rel="stylesheet">
<style>
:root{
  --green:#2fe08a;
  --green-dark:#1fc372;
  --ink:#2b2b33;
  --muted:#8a8d96;
  --line:#e4e6ea;
  --band:#f1f2f4;
  --night:#1b1428;
  --pink:#f5427a;
  --coral:#ff6f61;
  --cyan:#1fc4ef;
  --purple:#8a5cf6;
  --violet:#b04cf2;
  --soft-cyan:#7fd8f2;
  --soft-pink:#f5b3cb;
  --soft-yellow:#f8e49a;
  --footer:#1f1f22;
  --footer-text:#a9abb0;
}
*{box-sizing:border-box;margin:0;padding:0}
html,body{width:1200px;height:2756px;overflow:hidden}
body{font-family:"Open Sans",sans-serif;color:var(--ink);background:#fff;position:relative}
h1,h2,h3,h4{font-family:"Roboto",sans-serif}
.site-header{position:absolute;top:0;left:0;width:1200px;height:72px;display:flex;align-items:center;padding:0 130px;background:#fff}
.brand{display:flex;align-items:center;gap:12px;font-family:"Roboto",sans-serif;font-weight:700;font-size:17px;line-height:1.1;color:var(--ink);width:200px}
.brand-mark{width:34px;height:34px;border-radius:50%;background:var(--green);flex:none}
.main-nav{display:flex;gap:46px;margin-left:120px;font-size:14px;color:#555}
.btn-outline{margin-left:auto;border:2px solid var(--green);color:var(--green-dark);border-radius:22px;padding:9px 26px;font-size:13px;font-weight:600;text-transform:uppercase}
.hero{position:absolute;top:72px;left:0;width:1200px;height:448px;background:radial-gradient(ellipse at 30% 40%,#3a2a55 0%,var(--night) 60%,#0f0b18 100%)}
.hero-copy{position:absolute;left:140px;top:118px;width:440px}
.hero-title{color:#fff;font-size:44px;font-weight:700;line-height:1.15}
.btn-green{display:inline-block;background:var(--green);color:#fff;font-size:12px;font-weight:700;text-transform:uppercase;padding:12px 26px;border-radius:24px;letter-spacing:.5px}
.hero-copy .btn-green{margin-top:26px}
.hero-photo{position:absolute;left:620px;top:30px;width:580px;height:418px;background:linear-gradient(135deg,#e9dcc4 0%,#c9a27a 35%,#8e3b2e 60%,#2f5b4a 85%,#d8e3cf 100%)}
.section-title{text-align:center;font-size:30px;font-weight:500;color:var(--ink)}
.section-lead{text-align:center;font-size:13px;color:var(--muted);line-height:1.7;width:520px;margin:18px auto 0}
.features{position:absolute;top:520px;left:0;width:1200px;height:480px;padding-top:72px}
.feature-cards{display:flex;justify-content:center;gap:36px;margin-top:54px}
.feature-card{width:250px;height:220px;border:2px solid var(--green);border-radius:6px;text-align:center;padding-top:28px}
.feature-icon{width:54px;height:54px;border-radius:50%;margin:0 auto;background:linear-gradient(135deg,#ffd9a0,#f58a6b)}
.feature-card:nth-child(2) .feature-icon{background:linear-gradient(135deg,#fff0a8,#3fb7e8)}
.feature-card:nth-child(3) .feature-icon{background:linear-gradient(135deg,#ffe6a8,#f2b233)}
.feature-tag{font-size:11px;color:var(--green-dark);margin-top:12px}
.feature-name{font-size:19px;font-weight:500;margin-top:4px;letter-spacing:.5px}
.feature-text{font-size:12px;color:var(--muted);line-height:1.6;margin:10px 24px 0}
.about{position:absolute;top:1000px;left:0;width:1200px;height:400px;background:var(--band)}
.about-copy{position:absolute;left:130px;top:92px;width:460px}
.about-title{font-size:32px;font-weight:500}
.about-copy p{font-size:13px;color:var(--muted);line-height:1.7;margin-top:18px}
.about-copy .btn-green{margin-top:26px}
.book-cover{position:absolute;left:738px;top:24px;width:150px;height:326px;border-radius:2px 8px 8px 2px;background:linear-gradient(160deg,#1d2a55 0%,#3b3f9b 45%,#0d1230 100%);box-shadow:8px 10px 18px rgba(0,0,0,.25)}
.pricing{position:absolute;top:1400px;left:0;width:1200px;height:600px;padding-top:36px}
.plans{position:absolute;top:136px;left:236px;width:728px;height:420px}
.plan{position:absolute;background:#fff;box-shadow:0 6px 24px rgba(0,0,0,.12);text-align:center}
.plan-basic{left:0;top:30px;width:230px;height:340px}
.plan-standard{left:230px;top:0;width:250px;height:384px;z-index:2}
.plan-premium{left:480px;top:30px;width:230px;height:340px}
.plan-head{height:150px;color:#fff;padding-top:36px;clip-path:polygon(0 0,100% 0,100% 78%,0 100%)}
.plan-basic .plan-head{background:linear-gradient(135deg,var(--pink),var(--coral))}
.plan-standard .plan-head{height:170px;background:linear-gradient(135deg,#32d6f5,var(--cyan))}
.plan-premium .plan-head{background:linear-gradient(135deg,var(--purple),var(--violet))}
.plan-name{font-size:26px;font-weight:500;letter-spacing:1px}
.plan-price{font-family:"Roboto",sans-serif;font-size:40px;font-weight:500;margin-top:6px}
.plan-price sup{font-size:16px}
.plan-price small{font-size:12px}
.plan-features{list-style:none;text-align:left;padding:14px 22px 0}
.plan-features li{display:flex;gap:8px;font-size:10px;color:var(--muted);line-height:1.5;margin-bottom:12px}
.plan-features li::before{content:"";flex:none;width:10px;height:10px;border:1px solid #bbb;margin-top:2px}
.plan-btn{display:inline-block;color:#fff;font-size:11px;font-weight:700;padding:9px 22px;border-radius:18px;text-transform:uppercase}
.plan-basic .plan-btn{background:var(--pink)}
.plan-standard .plan-btn{background:var(--cyan)}
.plan-premium .plan-btn{background:var(--purple)}
.testimonial{position:absolute;top:2040px;left:0;width:1200px;height:360px}
.testimonial-bg{position:absolute;inset:0;background:linear-gradient(110deg,var(--soft-cyan) 0%,var(--soft-pink) 45%,var(--soft-pink) 65%,var(--soft-yellow) 100%)}
.testimonial-body{position:absolute;left:380px;top:88px;width:440px;text-align:center}
.testimonial-title{font-size:22px;font-weight:400;color:var(--ink);text-transform:uppercase}
.testimonial-title strong{font-weight:700}
.quote{position:relative;font-size:12px;color:#4a4d56;line-height:1.7;margin-top:26px;padding:0 30px}
.quote-mark{position:absolute;font-family:"Roboto",sans-serif;font-size:30px;font-weight:700;color:var(--ink);line-height:1}
.quote-open{left:0;top:-8px}
.quote-close{right:0;bottom:-22px}
.avatar{width:58px;height:58px;border-radius:50%;margin:16px auto 0;background:linear-gradient(135deg,#d9b8a0,#7a5a4a);border:3px solid #fff}
.person{font-size:13px;font-weight:600;margin-top:8px}
.site-footer{position:absolute;top:2400px;left:0;width:1200px;height:356px;background:var(--footer);color:var(--footer-text)}
.footer-cols{position:absolute;top:52px;left:130px;width:960px;display:flex}
.footer-col h4{color:#fff;font-size:16px;font-weight:500;letter-spacing:.5px;text-transform:uppercase;margin-bottom:18px}
.col-company{width:330px}
.col-company p{font-size:11px;line-height:1.7;width:280px}
.col-solutions{width:300px}
.link-grid{display:grid;grid-template-columns:90px 110px;row-gap:8px;font-size:12px}
.col-message{width:330px}
.message-row{display:flex;gap:10px}
.message-input{width:200px;height:30px;background:#fff;border-radius:15px}
.message-send{background:var(--green);color:#fff;font-size:11px;font-weight:700;border-radius:15px;padding:7px 20px}
.follow{display:flex;align-items:center;gap:10px;margin-top:36px;color:#fff;font-size:13px;font-weight:600}
.follow .dot{width:12px;height:12px;border-radius:50%;background:var(--cyan)}
.follow .dot:nth-child(3){background:var(--purple)}
.follow .dot:nth-child(4){background:var(--pink)}
.follow .dot:nth-child(5){background:var(--green)}
.follow .dot:nth-child(6){background:#f5a623}
.footer-bottom{position:absolute;bottom:0;left:0;width:1200px;height:42px;border-top:1px solid #333;display:flex;align-items:center;justify-content:space-between;padding:0 130px;font-size:10px}
</style>
</head>
<body>

<header class="site-header">
  <div class="brand"><span class="brand-mark"></span><span>Amber Ridge<br>Publishing</span></div>
  <nav class="main-nav"><span>Home</span><span>Features</span><span>Pricing</span><span>Our Products</span></nav>
  <span class="btn-outline">Contact us</span>
</header>

<section class="hero">
  <div class="hero-copy">
    <h1 class="hero-title">Let Us Help<br>You With All Of Your<br>Publishing Needs</h1>
    <span class="btn-green">Get a quote</span>
  </div>
  <div class="hero-photo" role="img" aria-label="Photo of a stack of books with an open book on top"></div>
</section>

<section class="features">
  <h2 class="section-title">Our Features</h2>
  <p class="section-lead">We shape every manuscript with care, from the first draft to the printed page, and help each title find readers who will love it.</p>
  <div class="feature-cards">
    <div class="feature-card">
      <div class="feature-icon" role="img" aria-label="Rocket icon"></div>
      <div class="feature-tag">Publish</div>
      <h3 class="feature-name">COOL PROJECTS</h3>
      <p class="feature-text">Bold ideas and clear plans for every book we release.</p>
    </div>
    <div class="feature-card">
      <div class="feature-icon" role="img" aria-label="Magnifying glass icon"></div>
      <div class="feature-tag">Publish</div>
      <h3 class="feature-name">EXCLUSIVE</h3>
      <p class="feature-text">Hand picked stories with a voice all of their own.</p>
    </div>
    <div class="feature-card">
      <div class="feature-icon" role="img" aria-label="Award ribbon icon"></div>
      <div class="feature-tag">Publish</div>
      <h3 class="feature-name">HIGH QUALITY</h3>
      <p class="feature-text">Careful editing, fine paper and lasting printed editions.</p>
    </div>
  </div>
</section>

<section class="about">
  <div class="about-copy">
    <h2 class="about-title">About Us</h2>
    <p>We are a small press built by readers for readers, bringing fresh voices in mystery and fiction to shelves around the world.</p>
    <p>Our editors, designers and marketers work side by side with every author so each story reaches its audience in the best possible shape.</p>
    <span class="btn-green">View products</span>
  </div>
  <div class="book-cover" role="img" aria-label="Book cover of Silent Ledger by M.R. Theodor"></div>
</section>

<section class="pricing">
  <h2 class="section-title">Choose Your Pricing Plans</h2>
  <p class="section-lead">Pick the plan that fits your book and budget. Every plan includes editing, layout and worldwide distribution.</p>
  <div class="plans">
    <div class="plan plan-basic">
      <div class="plan-head"><div class="plan-name">BASIC</div><div class="plan-price"><sup>$</sup>20<small>/Mon</small></div></div>
      <ul class="plan-features">
        <li>Professional editing and proofreading for your full manuscript.</li>
        <li>Simple interior layout in print and ebook formats.</li>
        <li>Listing with major online book retailers.</li>
      </ul>
      <span class="plan-btn">Buy now</span>
    </div>
    <div class="plan plan-standard">
      <div class="plan-head"><div class="plan-name">STANDARD</div><div class="plan-price"><sup>$</sup>35<small>/Mon</small></div></div>
      <ul class="plan-features">
        <li>Everything in Basic plus a custom designed cover.</li>
        <li>Launch plan with reviews and reader outreach.</li>
        <li>Print runs for local shops and book fairs.</li>
      </ul>
      <span class="plan-btn">Buy now</span>
    </div>
    <div class="plan plan-premium">
      <div class="plan-head"><div class="plan-name">PREMIUM</div><div class="plan-price"><sup>$</sup>50<small>/Mon</small></div></div>
      <ul class="plan-features">
        <li>Everything in Standard plus a dedicated editor.</li>
        <li>Audiobook production and worldwide distribution.</li>
        <li>Author tour planning and press support.</li>
      </ul>
      <span class="plan-btn">Buy now</span>
    </div>
  </div>
</section>

<section class="testimonial">
  <div class="testimonial-bg" role="img" aria-label="Decorative background of overlapping cyan, pink and yellow shapes"></div>
  <div class="testimonial-body">
    <h2 class="testimonial-title">Best publishers of <strong>top books</strong></h2>
    <p class="quote"><span class="quote-mark quote-open">&ldquo;</span>Having worked with Amber Ridge Publishing, I can say they are constantly moving forward with the best strategy for every author.<span class="quote-mark quote-close">&rdquo;</span></p>
    <div class="avatar" role="img" aria-label="Portrait of Daniel Hart"></div>
    <div class="person">Daniel Hart</div>
  </div>
</section>

<footer class="site-footer">
  <div class="footer-cols">
    <div class="footer-col col-company">
      <h4>Our Company</h4>
      <p>Amber Ridge Publishing is an independent press for mystery and fiction readers all over the world. We find great stories and help them travel far.</p>
    </div>
    <div class="footer-col col-solutions">
      <h4>Solutions</h4>
      <div class="link-grid">
        <span>About</span><span>Contact Us</span>
        <span>Customers</span><span>Knowledge Base</span>
        <span>Press</span><span>Privacy Policy</span>
        <span>Blog</span><span>Conditions</span>
      </div>
    </div>
    <div class="footer-col col-message">
      <h4>Send us a message</h4>
      <div class="message-row"><span class="message-input"></span><span class="message-send">SEND</span></div>
      <div class="follow"><span>FOLLOW US</span><span class="dot"></span><span class="dot"></span><span class="dot"></span><span class="dot"></span><span class="dot"></span></div>
    </div>
  </div>
  <div class="footer-bottom"><span>Copyright 2019 &copy; Amber Ridge Publishing</span><span>Privacy Policy &nbsp;|&nbsp; Terms &amp; Conditions</span></div>
</footer>

</body>
</html>
```